Easy - Fix our "Snag the Bash" Promo Flyer

Please see attached promo flyer with all the information required. Looking for quick assistance so we can go live with the advertising for this competition. Looking for something more commercial and polished. Very attractive so that lots of people enter the competition. <br/><br/>Happy for it to look a little bit festive as the competition is running in December. <br/><br/>Attached is out Fork Lodge Logo and first attempts at poster. Please let me know if you need anything further. <br/><br/>If you see any grammar or spelling errors please feel free to fix too.
Target Market(s)
Corporate Businesses who are buying vouchers as staff christmas gifts/bonus
Colors
Designer to choose colors to be used in the design.
Look and feel

```html
<!DOCTYPE html>
<html lang="en">
<head>
<meta charset="utf-8">
<title>Snag the Bash – Fork Lodge Staff Party Promo</title>
<link rel="stylesheet" href="https://fonts.googleapis.com/css2?family=Oswald:wght@400;500;600;700&family=Great+Vibes&family=Kaushan+Script&family=Open+Sans:ital,wght@0,400;0,600;1,600&display=swap">
<style>
  :root {
    --charcoal: #1d1d1f;
    --charcoal-light: #3a3a3d;
    --red-deep: #8e0a10;
    --red: #c8121a;
    --red-bright: #e3252c;
    --gold: #d9b35c;
    --gold-light: #f6dd94;
    --gold-dark: #a8762a;
    --cream: #f4ead6;
    --peach: #f6c48a;
    --white: #ffffff;
  }
  * { box-sizing: border-box; margin: 0; padding: 0; }
  html, body { width: 978px; height: 1200px; overflow: hidden; background: #ececec; }
  .flyer {
    position: relative; width: 978px; height: 1200px; overflow: hidden;
    font-family: "Oswald", sans-serif; color: var(--white);
  }
  .side-panel {
    position: absolute; left: 0; top: 0; width: 368px; height: 1200px;
    background: linear-gradient(180deg, var(--charcoal) 0%, var(--charcoal-light) 55%, var(--charcoal) 100%);
  }
  .ornaments-art {
    position: absolute; left: 30px; top: 0; width: 310px; height: 830px;
    background:
      radial-gradient(circle at 62% 38%, rgba(200,18,26,.85) 0 14%, transparent 15%),
      radial-gradient(circle at 30% 22%, rgba(200,18,26,.8) 0 13%, transparent 14%),
      radial-gradient(circle at 50% 68%, rgba(200,18,26,.85) 0 20%, transparent 21%),
      radial-gradient(ellipse at 50% 50%, rgba(217,179,92,.12), transparent 70%);
  }
  .xmas-greeting {
    position: absolute; left: 0; width: 368px; top: 905px; text-align: center;
    font-family: "Great Vibes", cursive; font-size: 36px; line-height: 1.2; color: var(--gold);
  }
  .brand-mark {
    position: absolute; left: 0; width: 368px; top: 1050px;
    display: flex; align-items: center; justify-content: center; gap: 12px;
  }
  .brand-mark .dot { width: 20px; height: 20px; border-radius: 50%; background: var(--red-bright); }
  .brand-mark .name { font-size: 48px; font-weight: 700; letter-spacing: 1px; color: var(--white); white-space: nowrap; }

  .promo-panel {
    position: absolute; left: 368px; top: 0; width: 610px; height: 1200px;
    background: radial-gradient(ellipse at 50% 30%, var(--red-bright) 0%, var(--red) 40%, var(--red-deep) 100%);
    text-align: center;
  }
  .promo-panel > * { position: absolute; left: 0; width: 100%; white-space: nowrap; }
  .headline-win {
    top: 28px; left: 48px; width: auto; text-align: left;
    font-size: 178px; font-weight: 700; line-height: 1; letter-spacing: -4px;
    background: linear-gradient(180deg, var(--gold-light), var(--gold) 50%, var(--gold-dark));
    -webkit-background-clip: text; background-clip: text; color: transparent;
  }
  .headline-ultimate { top: 164px; left: 304px; width: auto; text-align: left; font-size: 34px; font-weight: 400; line-height: 1.2; }
  .headline-party {
    top: 236px; font-size: 98px; font-weight: 700; line-height: 1.2; letter-spacing: 1px;
    background: linear-gradient(180deg, var(--white) 0%, var(--cream) 60%, var(--gold-light));
    -webkit-background-clip: text; background-clip: text; color: transparent;
  }
  .gold-rule { top: 370px; left: 42px; width: 528px; height: 4px; background: linear-gradient(90deg, var(--gold-dark), var(--gold-light), var(--gold-dark)); }
  .tagline { top: 392px; font-family: "Kaushan Script", cursive; font-size: 40px; line-height: 1.2; color: var(--gold); }
  .offer { font-size: 27px; font-weight: 500; line-height: 42px; text-transform: uppercase; }
  .offer-top { top: 504px; }
  .date-ribbon {
    top: 554px; left: 98px; width: 414px; height: 42px; line-height: 42px;
    font-size: 26px; font-weight: 500; color: var(--charcoal);
    background: linear-gradient(90deg, var(--gold-dark), var(--gold-light) 50%, var(--gold-dark));
    clip-path: polygon(0 0, 100% 0, 96% 50%, 100% 100%, 0 100%, 4% 50%);
  }
  .offer-bottom { top: 610px; }
  .details {
    font-family: "Open Sans", sans-serif; font-style: italic; font-weight: 600;
    font-size: 20px; line-height: 31px; color: var(--peach);
  }
  .details-prize { top: 752px; }
  .details-cake { top: 820px; }
  .voucher-row { top: 931px; display: flex; justify-content: center; gap: 16px; }
  .voucher-art { width: 176px; height: 58px; border-radius: 2px; box-shadow: 0 3px 6px rgba(0,0,0,.35); }
  .voucher-art.kraft { background: linear-gradient(90deg, #c9ad7f, #e7d4ae); }
  .voucher-art.yellow { background: linear-gradient(90deg, #f2c21b, #fbf4dc 40%, #ffffff); }
  .voucher-art.red { background: linear-gradient(90deg, #c8121a, #fbeeee 40%, #ffffff); }
  .tip { top: 1034px; font-size: 20px; font-weight: 400; line-height: 26px; text-transform: uppercase; }
  .fine-print { top: 1062px; font-family: "Open Sans", sans-serif; font-size: 14px; line-height: 21px; }
  .contact-bar {
    top: 1126px; display: flex; justify-content: center; gap: 48px;
    font-family: "Open Sans", sans-serif; font-size: 16px; align-items: center;
  }
  .contact-item { display: flex; align-items: center; gap: 8px; }
  .contact-item svg { width: 20px; height: 20px; }
  .social-dot { width: 18px; height: 18px; border-radius: 50%; background: var(--gold); }
</style>
</head>
<body>
<main class="flyer">
  <aside class="side-panel">
    <div class="ornaments-art" role="img" aria-label="Three red Christmas baubles with white snowflakes hanging on gold strings among gold sparkles"></div>
    <p class="xmas-greeting">Have a Merry Xmas<br>at The Fork Lodge</p>
    <div class="brand-mark"><span class="dot"></span><span class="name">FORK LODGE</span></div>
  </aside>

  <section class="promo-panel">
    <h1 class="headline-win">WIN</h1>
    <p class="headline-ultimate">THE ULTIMATE</p>
    <h2 class="headline-party">STAFF PARTY</h2>
    <div class="gold-rule"></div>
    <p class="tagline">For you and your colleagues</p>
    <p class="offer offer-top">Purchase K5,000 worth of vouchers before</p>
    <p class="date-ribbon">DECEMBER 31ST</p>
    <p class="offer offer-bottom">And go into the draw to win the ultimate staff<br>party for 150 people!</p>
    <p class="details details-prize">This includes a venue, BBQ-style PNG menu,<br>roast pig, decor &amp; much more...</p>
    <p class="details details-cake">We will even throw in an extra-large themed cake<br>with your company logo on it!</p>
    <div class="voucher-row">
      <div class="voucher-art kraft" role="img" aria-label="Kraft paper shopping voucher"></div>
      <div class="voucher-art yellow" role="img" aria-label="Yellow shopping voucher"></div>
      <div class="voucher-art red" role="img" aria-label="Red shopping voucher"></div>
    </div>
    <p class="tip">Tip: buy more vouchers to have better chances of winning</p>
    <p class="fine-print">*For every HR department enquiry we receive a special surprise will be given,<br>so hurry and contact us below on...</p>
    <div class="contact-bar">
      <span class="contact-item">
        <svg viewBox="0 0 20 20"><circle cx="10" cy="10" r="10" fill="#d9b35c"/><rect x="5" y="6.5" width="10" height="7" fill="none" stroke="#8e0a10" stroke-width="1.4"/><path d="M5 6.5l5 4 5-4" fill="none" stroke="#8e0a10" stroke-width="1.4"/></svg>
        sales@forklodge-eats.com
      </span>
      <span class="contact-item">
        <svg viewBox="0 0 20 20"><circle cx="10" cy="10" r="10" fill="#d9b35c"/><path d="M7 5l2 2.5-1.2 1.5a7 7 0 0 0 3.2 3.2l1.5-1.2L15 13l-1.5 2A9 9 0 0 1 5 6.5z" fill="#8e0a10"/></svg>
        7000 45100
      </span>
      <span class="contact-item"><span class="social-dot"></span>forklodgeeats</span>
    </div>
  </section>
</main>
</body>
</html>
```